Etiketten-Design für Wild Meadow Tangy Aioli gesucht
Zielgruppe
KRAUTHAFEN Würzig & Fein Food Market, Online Handel für BBQ- und Chili-Spezialitäten
Zielgruppe: Menschen die besonderen Wert auf qualitativ hochwertige Nahrungsmittel legen, die ohne sämtliche Zusatzstoffe- und Konservierungsstoffe auskommen. Die Hauptzielgruppe ist männlich und zwischen 30-50 Jahre alt.
Aufgabenstellung
Die Wild Meadow Tangy Aioli 'Dipping Galore' ist ein Bestseller in unserem Shop. Die Mayo wird aus Amerika importiert und ist eine pikante Mayo. Die Mayo gibt es bisher in einer pikanten Schärfe und soll noch zwei weitere Varianten mit Habanero Chilis und der schärfsten Chili der Welt, der Carolina Reaper, ergänzt werden.
Das Etikettenformat kann bis zu einer Größe von 170 x 100 mm betragen.
Bei dem neuen Design möchten wir keine Einschränkungen machen und der Kreativität freien Lauf lassen.

```html
<!DOCTYPE html>
<html lang="de">
<head>
<meta charset="utf-8">
<title>Dipping Galore – Etiketten</title>
<link rel="stylesheet" href="https://fonts.googleapis.com/css2?family=Bebas+Neue&family=Alfa+Slab+One&family=Pinyon+Script&family=Open+Sans:wght@400;700&display=swap">
<style>
  :root {
    --page: #e3e4e6;
    --chalk-light: #3b3b3b;
    --chalk-dark: #161616;
    --chalk-white: #f4f4f4;
    --text: #e9e9e9;
    --accent-red: #e0303a;
    --ornament: rgba(255,255,255,0.16);
    --pepper-red: #d9261f;
    --pepper-orange: #e07a1e;
    --pepper-yellow: #d9b43a;
    --leaf: #76b84a;
  }
  * { margin: 0; padding: 0; box-sizing: border-box; }
  html, body { width: 727px; height: 1200px; overflow: hidden; }
  body {
    background: radial-gradient(ellipse at 50% 55%, #f4f4f5 0%, var(--page) 70%);
    font-family: "Open Sans", sans-serif;
    position: relative;
  }
  .label {
    position: absolute;
    left: 55px;
    width: 617px;
    height: 363px;
    background: radial-gradient(ellipse at 50% 45%, var(--chalk-light) 0%, #252525 55%, var(--chalk-dark) 100%);
    color: var(--text);
    overflow: hidden;
  }
  .label--reaper { top: 37px; }
  .label--habanero { top: 410px; }
  .label--classic { top: 791px; }

  .frame { position: absolute; inset: 0; width: 617px; height: 363px; }
  .ornament {
    position: absolute;
    background: var(--ornament);
    border-radius: 40% 60% 50% 50% / 60% 40% 60% 40%;
  }
  .ornament--tl { left: 8px; top: 8px; width: 165px; height: 62px; }
  .ornament--tr { right: 8px; top: 8px; width: 165px; height: 56px; }
  .ornament--bl { left: 8px; bottom: 12px; width: 165px; height: 58px; }
  .ornament--br { right: 8px; bottom: 12px; width: 165px; height: 58px; }
  .ornament--crown { left: 200px; top: 6px; width: 215px; height: 22px; }
  .ornament--wreath {
    left: 196px; top: 118px; width: 225px; height: 205px;
    background: transparent;
    border: 3px solid rgba(255,255,255,0.22);
    border-radius: 50%;
  }

  .intro { position: absolute; left: 40px; top: 72px; width: 112px; }
  .intro__script {
    font-family: "Pinyon Script", cursive;
    font-size: 22px;
    line-height: 20px;
    color: var(--chalk-white);
    margin-bottom: 12px;
  }
  .intro__body { font-size: 7.1px; line-height: 8.9px; }

  .brand { position: absolute; left: 0; width: 617px; top: 44px; text-align: center; }
  .brand__name {
    font-family: "Bebas Neue", sans-serif;
    font-size: 42px;
    line-height: 40px;
    color: var(--chalk-white);
    letter-spacing: 1px;
  }
  .brand__variant {
    font-family: "Alfa Slab One", serif;
    font-size: 20px;
    line-height: 24px;
    color: var(--accent-red);
  }

  .pepper {
    position: absolute;
    left: 232px; top: 132px; width: 155px; height: 178px;
    border-radius: 45% 45% 40% 40%;
  }
  .pepper--reaper { background: linear-gradient(100deg, var(--pepper-orange) 0%, var(--pepper-orange) 40%, var(--leaf) 48%, var(--pepper-red) 55%, var(--pepper-red) 100%); }
  .pepper--habanero { background: linear-gradient(100deg, var(--pepper-yellow) 0%, var(--pepper-yellow) 38%, var(--leaf) 45%, var(--pepper-red) 52%, #c8321d 100%); }
  .pepper--classic { background: linear-gradient(135deg, var(--pepper-yellow) 0%, var(--leaf) 35%, var(--pepper-red) 55%, var(--pepper-yellow) 85%); border-radius: 50%; }

  .tagline {
    position: absolute; left: 0; width: 617px; top: 322px;
    text-align: center;
    font-family: "Pinyon Script", cursive;
    font-size: 24px;
    line-height: 30px;
    color: var(--chalk-white);
  }

  .facts { position: absolute; left: 463px; top: 68px; width: 119px; text-align: right; font-size: 7.1px; line-height: 8.9px; }
  .facts__title { font-size: 10.5px; line-height: 12px; font-weight: 700; }
  .facts__ingredients { width: 104px; margin-left: auto; }
  .facts__divider { border-top: 1px dotted rgba(255,255,255,0.7); width: 90px; margin: 14px 6px 14px auto; }
  .facts__table-title { font-size: 9px; font-weight: 700; margin-bottom: 10px; text-align: left; }
  .facts__table-title span { font-weight: 400; font-size: 7.1px; }
</style>
</head>
<body>

<section class="label label--reaper">
  <div class="ornament ornament--tl" role="img" aria-label="Weiße Kreideschnörkel, Ecke oben links"></div>
  <div class="ornament ornament--tr" role="img" aria-label="Weiße Kreideschnörkel, Ecke oben rechts"></div>
  <div class="ornament ornament--bl" role="img" aria-label="Weiße Kreideschnörkel, Ecke unten links"></div>
  <div class="ornament ornament--br" role="img" aria-label="Weiße Kreideschnörkel, Ecke unten rechts"></div>
  <div class="ornament ornament--crown" role="img" aria-label="Blattornament über dem Markennamen"></div>
  <div class="ornament ornament--wreath" role="img" aria-label="Schnörkelkranz um die Chili-Illustration"></div>
  <svg class="frame" viewBox="0 0 617 363" aria-hidden="true">
    <g stroke="#f4f4f4" stroke-width="2.5" fill="none">
      <line x1="22" y1="88" x2="22" y2="258"/><line x1="592" y1="95" x2="592" y2="265"/>
      <path d="M170 58 Q308 18 450 58"/>
      <path d="M175 114 Q195 104 218 99"/><path d="M399 99 Q422 104 442 114"/>
    </g>
  </svg>
  <div class="intro">
    <p class="intro__script">Wild Meadow<br>Tangy Aioli</p>
    <p class="intro__body">Dipping Galore ist eine ganz natürliche Sauce, perfekt für, naja, fast alles! Als würzige Würze für Burger oder Sandwiches, als Dip für Gemüse, das frechste Salatdressing der Welt, als würzige Mayo, oder mit einer Garnele werfen und mehr! Dipping Galore is an all natural sauce perfect for, well, just about everthing! Use as a spiced up condiment for burgers or sandwiches, as a dip vor veggies, the sauciest salad dressing around, as a tangy mayo, or toss with scrimp and more!</p>
  </div>
  <div class="brand">
    <h1 class="brand__name">Dipping Galore</h1>
    <p class="brand__variant">Carolina Reaper</p>
  </div>
  <div class="pepper pepper--reaper" role="img" aria-label="Illustration: orange und rote Carolina-Reaper-Chilis mit grünen Blättern"></div>
  <p class="tagline">Wild Meadow Tangy Aioli</p>
  <div class="facts">
    <p class="facts__title">Carolina Reaper</p>
    <p class="facts__ingredients">Soja- und Rapsöl, Eigelb, Essig, Wasser, Chai-Tee, Thai-Chilis, Rohrzucker, Knoblauch, Carolina Reaper Chilis, Salz, Reisessig, Zitronensaft, Stärke, Petersilie, natürliche Gewürze.</p>
    <div class="facts__divider"></div>
    <p class="facts__table-title">Nährwert-Tabelle: <span>je 100 g</span></p>
    <p>Brennwert xx kJ / Energie xx kcal<br>Fett x, x g, - davon gesättigte<br>Fettsäuren x,x g,<br>Kohlenhydrate xx,x g,<br>- davon Zucker x,x g<br>Eiweiß x,x g<br>Salz x,x g<br>Nach dem Öffnen kühl lagern.<br>Vor Gebrauch gut schütteln.</p>
  </div>
</section>

<section class="label label--habanero">
  <div class="ornament ornament--tl" role="img" aria-label="Weiße Kreideschnörkel, Ecke oben links"></div>
  <div class="ornament ornament--tr" role="img" aria-label="Weiße Kreideschnörkel, Ecke oben rechts"></div>
  <div class="ornament ornament--bl" role="img" aria-label="Weiße Kreideschnörkel, Ecke unten links"></div>
  <div class="ornament ornament--br" role="img" aria-label="Weiße Kreideschnörkel, Ecke unten rechts"></div>
  <div class="ornament ornament--crown" role="img" aria-label="Blattornament über dem Markennamen"></div>
  <div class="ornament ornament--wreath" role="img" aria-label="Schnörkelkranz um die Chili-Illustration"></div>
  <svg class="frame" viewBox="0 0 617 363" aria-hidden="true">
    <g stroke="#f4f4f4" stroke-width="2.5" fill="none">
      <line x1="22" y1="88" x2="22" y2="258"/><line x1="592" y1="95" x2="592" y2="265"/>
      <path d="M170 58 Q308 18 450 58"/>
      <path d="M175 114 Q205 104 245 99"/><path d="M372 99 Q412 104 442 114"/>
    </g>
  </svg>
  <div class="intro">
    <p class="intro__script">Wild Meadow<br>Tangy Aioli</p>
    <p class="intro__body">Dipping Galore ist eine ganz natürliche Sauce, perfekt für, naja, fast alles! Als würzige Würze für Burger oder Sandwiches, als Dip für Gemüse, das frechste Salatdressing der Welt, als würzige Mayo, oder mit einer Garnele werfen und mehr! Dipping Galore is an all natural sauce perfect for, well, just about everthing! Use as a spiced up condiment for burgers or sandwiches, as a dip vor veggies, the sauciest salad dressing around, as a tangy mayo, or toss with scrimp and more!</p>
  </div>
  <div class="brand">
    <h1 class="brand__name">Dipping Galore</h1>
    <p class="brand__variant">Habanero</p>
  </div>
  <div class="pepper pepper--habanero" role="img" aria-label="Illustration: gelbe und rote Habanero-Chilis mit grünen Blättern"></div>
  <p class="tagline">Wild Meadow Tangy Aioli</p>
  <div class="facts">
    <p class="facts__title">Habanero</p>
    <p class="facts__ingredients">Soja- und Rapsöl, Eigelb, Essig, Wasser, Chai-Tee, Thai-Chilis, Rohrzucker, Knoblauch, Habanero Chilis, Salz, Reisessig, Zitronensaft, Stärke, Petersilie, natürliche Gewürze.</p>
    <div class="facts__divider"></div>
    <p class="facts__table-title">Nährwert-Tabelle: <span>je 100 g</span></p>
    <p>Brennwert xx kJ / Energie xx kcal<br>Fett x, x g, - davon gesättigte<br>Fettsäuren x,x g,<br>Kohlenhydrate xx,x g,<br>- davon Zucker x,x g<br>Eiweiß x,x g<br>Salz x,x g<br>Nach dem Öffnen kühl lagern.<br>Vor Gebrauch gut schütteln.</p>
  </div>
</section>

<section class="label label--classic">
  <div class="ornament ornament--tl" role="img" aria-label="Weiße Kreideschnörkel, Ecke oben links"></div>
  <div class="ornament ornament--tr" role="img" aria-label="Weiße Kreideschnörkel, Ecke oben rechts"></div>
  <div class="ornament ornament--bl" role="img" aria-label="Weiße Kreideschnörkel, Ecke unten links"></div>
  <div class="ornament ornament--br" role="img" aria-label="Weiße Kreideschnörkel, Ecke unten rechts"></div>
  <div class="ornament ornament--crown" role="img" aria-label="Blattornament über dem Markennamen"></div>
  <div class="ornament ornament--wreath" role="img" aria-label="Schnörkelkranz um die Chili-Illustration"></div>
  <svg class="frame" viewBox="0 0 617 363" aria-hidden="true">
    <g stroke="#f4f4f4" stroke-width="2.5" fill="none">
      <line x1="22" y1="88" x2="22" y2="258"/><line x1="592" y1="95" x2="592" y2="265"/>
      <path d="M170 58 Q308 18 450 58"/>
      <path d="M175 114 Q215 104 262 99"/><path d="M355 99 Q402 104 442 114"/>
    </g>
  </svg>
  <div class="intro">
    <p class="intro__script">Wild Meadow<br>Tangy Aioli</p>
    <p class="intro__body">Dipping Galore ist eine ganz natürliche Sauce, perfekt für, naja, fast alles! Als würzige Würze für Burger oder Sandwiches, als Dip für Gemüse, das frechste Salatdressing der Welt, als würzige Mayo, oder mit einer Garnele werfen und mehr! Dipping Galore is an all natural sauce perfect for, well, just about everthing! Use as a spiced up condiment for burgers or sandwiches, as a dip vor veggies, the sauciest salad dressing around, as a tangy mayo, or toss with scrimp and more!</p>
  </div>
  <div class="brand">
    <h1 class="brand__name">Dipping Galore</h1>
    <p class="brand__variant">Classic</p>
  </div>
  <div class="pepper pepper--classic" role="img" aria-label="Illustration: lange gelbe und rote Chilischoten mit grünen Blättern"></div>
  <p class="tagline">Wild Meadow Tangy Aioli</p>
  <div class="facts">
    <p class="facts__title">Classic</p>
    <p class="facts__ingredients">Soja- und Rapsöl, Eigelb, Essig, Wasser, Chai-Tee, Thai-Chilis, Rohrzucker, Knoblauch, Jalapeno Chilis, Salz, Reisessig, Zitronensaft, Stärke, Petersilie, natürliche Gewürze.</p>
    <div class="facts__divider"></div>
    <p class="facts__table-title">Nährwert-Tabelle: <span>je 100 g</span></p>
    <p>Brennwert xx kJ / Energie xx kcal<br>Fett x, x g, - davon gesättigte<br>Fettsäuren x,x g,<br>Kohlenhydrate xx,x g,<br>- davon Zucker x,x g<br>Eiweiß x,x g<br>Salz x,x g<br>Nach dem Öffnen kühl lagern.<br>Vor Gebrauch gut schütteln.</p>
  </div>
</section>

</body>
</html>
```